Cedar Hall letterhead

We changed our name and logo now need letterhead.
3-4/82 Marlow Street Larkfield 2391
www.cedarhall.org.au
info@cedarhall.org.au
ph: 02 95738127

At this stage, we are preferencing Design #: 5398880 and Design #5401338

```html
<!DOCTYPE html>
<html lang="en">
<head>
<meta charset="utf-8">
<title>Cedar Hall Letterhead Concepts</title>
<link rel="stylesheet" href="https://fonts.googleapis.com/css2?family=Open+Sans:wght@400;600&family=Raleway:wght@400&display=swap">
<style>
  :root {
    --board: #a7b7c6;
    --slate: #7a8797;
    --slate-edge: #6f7c8d;
    --mist: #a9b9c9;
    --name: #9aa8b8;
    --contact: #7d8590;
    --paper: #ffffff;
    --paper-soft: #f4f4f6;
    --pale-edge: #cdd4dd;
  }
  * { margin: 0; padding: 0; box-sizing: border-box; }
  html, body { width: 878px; height: 1200px; overflow: hidden; }
  body { background: var(--board); position: relative; font-family: "Open Sans", Arial, sans-serif; }

  .sheet { position: absolute; width: 378px; height: 536px; background: var(--paper); overflow: hidden; }
  .sheet--framed { border: 3px solid var(--slate-edge); }
  .sheet--soft { border: 2px solid var(--pale-edge); background: var(--paper-soft); }
  .sheet--tl { left: 31px; top: 31px; }
  .sheet--tr { left: 467px; top: 31px; }
  .sheet--bl { left: 31px; top: 640px; }
  .sheet--br { left: 467px; top: 640px; }

  .seal { position: absolute; width: 62px; height: 62px; border-radius: 50%; background: var(--slate);
          display: flex; align-items: center; justify-content: center; }
  .seal__name { font-family: "Raleway", Arial, sans-serif; font-size: 8px; letter-spacing: 1px; color: #ffffff; white-space: nowrap; }

  .brand-name { position: absolute; font-family: "Raleway", Arial, sans-serif; font-size: 14px;
                letter-spacing: 2px; color: var(--name); white-space: nowrap; }

  .contact { position: absolute; font-size: 6.5px; line-height: 8.4px; color: var(--contact); letter-spacing: 0.3px; white-space: nowrap; }

  .artwork { position: absolute; }
  .artwork--figure { left: 190px; top: 75px; width: 185px; height: 458px;
                     background: radial-gradient(ellipse at 55% 45%, #e6e6e8 0%, #efeff1 45%, rgba(255,255,255,0) 75%); }
  .artwork--bird { left: 15px; top: 315px; width: 345px; height: 215px;
                   background: radial-gradient(ellipse at 55% 55%, #e2e3e5 0%, #ededef 45%, rgba(255,255,255,0) 78%); }
  .artwork--pattern { left: 0; top: 0; width: 100%; height: 100%;
                      background: linear-gradient(90deg, #f1f1f3, #f6f6f8, #f1f1f3); }
  .artwork--floral { left: 0; bottom: 0; width: 165px; height: 162px;
                     background: radial-gradient(circle at 30% 70%, #d9dadf 0%, #e3e4e8 50%, rgba(244,244,246,0) 75%); }

  .curves { position: absolute; left: 0; top: 0; width: 378px; height: 536px; }
</style>
</head>
<body>

  <section class="sheet sheet--framed sheet--tl" aria-label="Letterhead concept one">
    <div class="artwork artwork--figure" role="img" aria-label="Faded white statue of a robed figure"></div>
    <div class="seal" style="left:11px; top:11px;"></div>
    <div class="brand-name" style="left:88px; top:34px;">CEDAR HALL</div>
    <div class="contact" style="left:12px; top:486px;">
      3-4/82 Marlow Street Larkfield 2391<br>www.cedarhall.org.au<br>info@cedarhall.org.au<br>ph: 02 95738127
    </div>
  </section>

  <section class="sheet sheet--framed sheet--tr" aria-label="Letterhead concept two">
    <div class="artwork artwork--bird" role="img" aria-label="Faded hummingbird feeding at a flowering stem"></div>
    <div class="seal" style="left:155px; top:12px;"></div>
    <div class="brand-name" style="left:228px; top:15px;">CEDAR HALL</div>
    <div class="contact" style="left:228px; top:37px;">
      3-4/82 Marlow Street Larkfield 2391<br>www.cedarhall.org.au<br>info@cedarhall.org.au<br>ph: 02 95738127
    </div>
  </section>

  <section class="sheet sheet--soft sheet--bl" aria-label="Letterhead concept three">
    <div class="artwork artwork--pattern" role="img" aria-label="Subtle vertical scalloped pattern background"></div>
    <div class="artwork artwork--floral" role="img" aria-label="Pale floral vine ornament in the corner"></div>
    <div class="seal" style="left:156px; top:8px;"><span class="seal__name">CEDAR HALL</span></div>
    <div class="contact" style="left:236px; top:494px;">
      3-4/82 Marlow Street Larkfield 2391<br>www.cedarhall.org.au<br>info@cedarhall.org.au<br>ph: 02 95738127
    </div>
  </section>

  <section class="sheet sheet--br" aria-label="Letterhead concept four">
    <svg class="curves" viewBox="0 0 378 536" aria-hidden="true">
      <path d="M0 0 H378 V34 Q189 70 0 34 Z" fill="var(--slate)"/>
      <path d="M0 46 Q189 84 378 46" fill="none" stroke="var(--slate)" stroke-width="6"/>
      <path d="M95 88 Q189 96 282 88 Q189 112 95 88 Z" fill="var(--mist)"/>
      <circle cx="189" cy="38" r="42" fill="#ffffff"/>
      <path d="M0 480 Q189 522 378 480 V536 H0 Z" fill="var(--slate)"/>
      <path d="M65 486 Q189 500 315 492 Q189 512 65 486 Z" fill="var(--mist)"/>
    </svg>
    <div class="seal" style="left:158px; top:7px;"><span class="seal__name">CEDAR HALL</span></div>
  </section>

</body>
</html>
```